Harbourlight Dental Centre Kelvale business cards and presentation folder

dental practice needing innovative black business cards for 2 different dentists witrh appointment details written at the back of the card for the patient.
name of dentists: Dr Anjali R Venkatesan B.D.S., M.P.H (Melb)
Dr. Raj Kalpat B.D.S.

Target Market(s)

professioinal, working class

Industry/Entity Type

Dental Clinic

Contact Information for Business Card

Dr. Raj Kalpat B.D.S.

Font styles to use
Sans Serif

Requirements
Must have
• Front side: logo
• dentist name
• phone number: 07- 5918 2243
• back side: appointment details: date, time,
• Address: 117C, 58 Tarrow Street, Kelvale - 4561, Queensland
• Email: admin@harbourlightdentalkelvale.example.au
• Website: www.harbourlightdental.example.au
• preferable logo colors
Nice to have
• classy look more pleasing

```html
<!DOCTYPE html>
<html lang="en">
<head>
<meta charset="utf-8">
<title>Harbourlight Dental Centre Kelvale – Business Card</title>
<link href="https://fonts.googleapis.com/css2?family=Cinzel:wght@500&family=Roboto+Condensed:wght@300;400;700&family=Yanone+Kaffeesatz:wght@500;700&display=swap" rel="stylesheet">
<style>
  :root {
    --stage: #e9e7e2;
    --card-black: #1c1c1d;
    --card-black-light: #343436;
    --leaf: #9cc47a;
    --leaf-deep: #7fa95e;
    --silver: #b9bcc2;
    --mist: #e3efdc;
    --ink: #161616;
    --text-light: #d9d9d9;
    --rule: #8a8f88;
  }
  * { box-sizing: border-box; margin: 0; padding: 0; }
  html, body { width: 1200px; height: 950px; overflow: hidden; }
  body {
    background: var(--stage);
    font-family: "Roboto Condensed", Arial, sans-serif;
    position: relative;
  }
  .card {
    position: absolute;
    left: 220px;
    width: 760px;
    height: 434px;
    border-radius: 22px;
    overflow: hidden;
    box-shadow: 0 10px 28px rgba(0,0,0,.22);
  }
  .card--front { top: 36px; background: radial-gradient(ellipse at 30% 40%, var(--card-black-light), var(--card-black) 70%); }
  .card--back { top: 490px; background: var(--mist); }

  .front-curves { position: absolute; inset: 0; width: 100%; height: 100%; }

  .brand { position: absolute; display: flex; align-items: center; gap: 12px; }
  .brand__dot { width: 16px; height: 16px; border-radius: 50%; background: var(--leaf); flex: none; }
  .brand__name {
    font-family: "Cinzel", Georgia, serif;
    font-weight: 500;
    line-height: 1.15;
    letter-spacing: 1px;
    white-space: nowrap;
  }
  .card--front .brand { left: 60px; top: 160px; }
  .card--front .brand__name { color: var(--text-light); font-size: 23px; }
  .card--back .brand { left: 150px; top: 46px; }
  .card--back .brand__name { color: var(--leaf-deep); font-size: 30px; }

  .address {
    position: absolute; left: 62px; top: 240px;
    color: var(--text-light); font-weight: 300; font-size: 19px; line-height: 1.3;
  }
  .contact {
    position: absolute; left: 62px; top: 330px; list-style: none;
    color: var(--text-light); font-weight: 300; font-size: 16px; line-height: 1.5;
  }
  .contact li { display: flex; align-items: center; gap: 10px; }
  .contact svg { width: 14px; height: 14px; flex: none; }

  .dentists {
    position: absolute; right: 196px; top: 32px; text-align: right;
    font-family: "Yanone Kaffeesatz", "Arial Narrow", sans-serif; color: var(--leaf);
  }
  .dentist__name { font-weight: 700; font-size: 28px; line-height: 1; }
  .dentist__quals { font-weight: 500; font-size: 17px; letter-spacing: 1px; line-height: 1.2; margin-bottom: 4px; }

  .appointment { position: absolute; left: 150px; top: 196px; width: 470px; }
  .appointment__title {
    font-weight: 700; font-size: 25px; color: var(--ink); letter-spacing: .5px; margin-bottom: 34px;
  }
  .appointment__field {
    display: flex; align-items: flex-end; gap: 8px; font-size: 18px; color: #444; margin-bottom: 38px;
  }
  .appointment__line { flex: 1; border-bottom: 2px dotted var(--rule); height: 18px; }
</style>
</head>
<body>

<section class="card card--front" aria-label="Business card front">
  <svg class="front-curves" viewBox="0 0 760 434" preserveAspectRatio="none" aria-hidden="true">
    <path d="M560 0 H760 V434 H700 C740 300 700 110 560 0 Z" fill="var(--leaf)"/>
    <path d="M500 0 H600 C700 90 745 260 690 434 H640 C700 280 640 90 500 0 Z" fill="var(--silver)"/>
    <path d="M470 0 H540 C660 100 700 270 655 434 H620 C665 270 610 100 470 0 Z" fill="#0f0f10"/>
  </svg>

  <div class="dentists">
    <p class="dentist__name">Dr Anjali R Venkatesan</p>
    <p class="dentist__quals">B.D.S., M.P.H (Melb)</p>
    <p class="dentist__name">Dr. Raj Kalpat <span class="dentist__quals">B.D.S.</span></p>
  </div>

  <div class="brand">
    <span class="brand__dot"></span>
    <p class="brand__name">HARBOURLIGHT DENTAL<br>CENTRE</p>
  </div>

  <p class="address">117C, 58 Tarrow Street<br>Kelvale - 4561<br>Queensland</p>

  <ul class="contact">
    <li>
      <svg viewBox="0 0 16 16"><path d="M4 1 L6 5 L4.5 6.5 C5.5 8.5 7.5 10.5 9.5 11.5 L11 10 L15 12 L13.5 15 C7 14.5 1.5 9 1 2.5 Z" fill="var(--leaf)"/></svg>
      07- 5918 2243
    </li>
    <li>
      <svg viewBox="0 0 16 16"><rect x="1" y="3" width="14" height="10" rx="1.5" fill="var(--leaf)"/><path d="M1.5 4 L8 9 L14.5 4" stroke="#1c1c1d" stroke-width="1.4" fill="none"/></svg>
      admin@harbourlightdentalkelvale.example.au
    </li>
    <li>
      <svg viewBox="0 0 16 16"><circle cx="8" cy="8" r="7" fill="var(--leaf)"/><path d="M1 8 H15 M8 1 C4.5 5 4.5 11 8 15 M8 1 C11.5 5 11.5 11 8 15" stroke="#1c1c1d" stroke-width="1" fill="none"/></svg>
      www.harbourlightdental.example.au
    </li>
  </ul>
</section>

<section class="card card--back" aria-label="Business card back">
  <div class="brand">
    <span class="brand__dot"></span>
    <p class="brand__name">HARBOURLIGHT DENTAL<br>CENTRE</p>
  </div>

  <div class="appointment">
    <h2 class="appointment__title">NEXT APPOINTMENT</h2>
    <p class="appointment__field">Date: <span class="appointment__line"></span></p>
    <p class="appointment__field">Time: <span class="appointment__line"></span> AM/PM</p>
  </div>
</section>

</body>
</html>
```